Business Card Design Project

Tarvolink - based in Melbourne, Australia. We plan, design, implement and support network infrastructure (Plemba, Hollvask, Q8, Stormpike etc).

Target Market(s)

Small/Medium enterprise and Corporate.

Industry/Entity Type

Business

```html
<!DOCTYPE html>
<html lang="en">
<head>
<meta charset="utf-8">
<title>Tarvolink Business Card</title>
<link rel="stylesheet" href="https://fonts.googleapis.com/css2?family=Lato:wght@400;700;900&display=swap">
<style>
  :root {
    --bg: #2b2b2b;
    --card: #ffffff;
    --card-shade: #e6e6e6;
    --orange: #e0870f;
    --orange-deep: #c86f0a;
    --grey: #5d5d5d;
    --grey-line: #707070;
    --text: #4a4a4a;
  }
  * { box-sizing: border-box; margin: 0; padding: 0; }
  html, body { width: 1200px; height: 997px; overflow: hidden; }
  body {
    background: var(--bg);
    font-family: "Lato", Arial, sans-serif;
    position: relative;
  }
  .card {
    position: absolute;
    left: 250px;
    width: 700px;
    height: 400px;
    border-radius: 22px;
    background: linear-gradient(180deg, var(--card) 0%, var(--card-shade) 100%);
    overflow: hidden;
    box-shadow: 0 14px 30px rgba(0,0,0,0.5);
  }
  .card--front { top: 70px; }
  .card--back { top: 527px; }

  /* front */
  .front-band {
    position: absolute; left: 0; top: 0; width: 100%; height: 52px;
    background: linear-gradient(90deg, var(--orange-deep), var(--orange));
  }
  .front-rule {
    position: absolute; left: 0; top: 52px; width: 100%; height: 7px;
    background: var(--grey-line);
  }
  .brand {
    position: absolute; display: flex; align-items: center;
    color: var(--orange); font-weight: 700;
  }
  .brand__mark { border-radius: 50%; border: solid var(--orange); }
  .front-brand { left: 0; right: 0; top: 175px; justify-content: center; gap: 20px; font-size: 92px; }
  .front-brand .brand__mark { width: 84px; height: 84px; border-width: 8px; }

  /* back */
  .back-brand { left: 0; right: 0; top: 36px; justify-content: center; gap: 12px; font-size: 44px; }
  .back-brand .brand__mark { width: 40px; height: 40px; border-width: 4px; }
  .person { position: absolute; left: 40px; top: 196px; width: 264px; text-align: right; }
  .person__name { color: var(--orange); font-weight: 900; font-size: 27px; letter-spacing: 0.5px; }
  .person__title { color: var(--text); font-weight: 700; font-size: 20px; margin-top: 2px; }
  .divider {
    position: absolute; left: 334px; top: 110px; width: 4px; height: 160px;
    background: linear-gradient(180deg, rgba(224,135,15,0.1), var(--orange) 45%, rgba(224,135,15,0.1));
  }
  .contacts { position: absolute; left: 360px; top: 110px; list-style: none; }
  .contacts li {
    display: flex; align-items: flex-start; gap: 10px;
    color: var(--text); font-size: 17px; line-height: 1.3; margin-bottom: 9px;
  }
  .contacts svg { flex: 0 0 24px; width: 24px; height: 24px; }
  .back-rule {
    position: absolute; left: 0; top: 300px; width: 100%; height: 8px;
    background: var(--grey-line);
  }
  .back-band {
    position: absolute; left: 0; top: 308px; width: 100%; height: 92px;
    background: linear-gradient(90deg, var(--orange), var(--orange-deep));
    display: flex; align-items: center; justify-content: center;
  }
  .website { color: #fbe3c4; font-size: 19px; font-weight: 700; letter-spacing: 6px; }
</style>
</head>
<body>
  <section class="card card--front" aria-label="Card front">
    <div class="front-band"></div>
    <div class="front-rule"></div>
    <div class="brand front-brand"><span class="brand__mark"></span><span>tarvolink</span></div>
  </section>

  <section class="card card--back" aria-label="Card back">
    <div class="brand back-brand"><span class="brand__mark"></span><span>tarvolink</span></div>
    <div class="person">
      <div class="person__name">MARCUS HALE</div>
      <div class="person__title">Vice President</div>
    </div>
    <div class="divider"></div>
    <ul class="contacts">
      <li>
        <svg viewBox="0 0 24 24"><circle cx="12" cy="12" r="12" fill="#5d5d5d"/><path d="M8 6.5l2.2 2.6-1.2 1.4c.8 1.8 2 3 3.6 3.8l1.4-1.2 2.6 2.2-1.3 2c-4.6-.6-8.3-4.3-8.9-8.8z" fill="#fff"/></svg>
        <span>03-9555-0142 x214</span>
      </li>
      <li>
        <svg viewBox="0 0 24 24"><circle cx="12" cy="12" r="12" fill="#5d5d5d"/><rect x="6" y="8" width="12" height="8" fill="none" stroke="#fff" stroke-width="1.4"/><path d="M6 8l6 5 6-5" fill="none" stroke="#fff" stroke-width="1.4"/></svg>
        <span>1800-555-019</span>
      </li>
      <li>
        <svg viewBox="0 0 24 24"><circle cx="12" cy="12" r="12" fill="#5d5d5d"/><path d="M10.5 13.5l3-3M9 12l-1.5 1.5a2.1 2.1 0 003 3L12 15M15 12l1.5-1.5a2.1 2.1 0 00-3-3L12 9" fill="none" stroke="#fff" stroke-width="1.5" stroke-linecap="round"/></svg>
        <span>mhale@tarvolink.com.au</span>
      </li>
      <li>
        <svg viewBox="0 0 24 24"><circle cx="12" cy="12" r="12" fill="#5d5d5d"/><path d="M12 18s-4-4.3-4-7.2a4 4 0 018 0C16 13.7 12 18 12 18z" fill="#fff"/><circle cx="12" cy="10.8" r="1.5" fill="#5d5d5d"/></svg>
        <span>57 Keelan Street, Level 3<br>Brunswick, VIC,<br>Australia, 3056</span>
      </li>
    </ul>
    <div class="back-rule"></div>
    <div class="back-band"><span class="website">www.tarvolink.com.au</span></div>
  </section>
</body>
</html>
```